Plakate zur Kugeltisch-Treffen mit Nordwall-Pokal der Tischkugel
Zielgruppe
Plakat zur Kugeltisch-Treffen mit Nordwall-Pokal der Tischkugel
Aufgabenstellung
Größe DIN A1
Kugeltisch Treffen 2023 mit offener Nordwall-Tischkugelpokal
in 17492 Lindenhain/Hofbrück
Donnerstag 18. Mai 2023 - Sonntag 21. Mai 2023
Viele Turniere für jedermann
Große Tombola mit einem Flipper als Hauptgewinn
Flippershops und Zubehör
Zeitplan und weitere Informationen auf www.kugelrunde-ost.de

```html
<!DOCTYPE html>
<html lang="de">
<head>
<meta charset="utf-8">
<title>Kugeltisch Treffen 2023 – Plakat</title>
<link rel="stylesheet" href="https://fonts.googleapis.com/css2?family=Poppins:wght@600;700;800&family=Open+Sans:wght@600;700&family=Great+Vibes&display=swap">
<style>
  :root {
    --black: #0a090a;
    --ink: #111011;
    --red: #c8102e;
    --white: #f2f2f2;
    --green: #1f9d3a;
    --photo-warm: #5a4a2e;
    --photo-mid: #2b2a30;
  }
  * { margin: 0; padding: 0; box-sizing: border-box; }
  html, body { width: 1000px; height: 1200px; overflow: hidden; background: var(--black); }
  .poster {
    position: relative; width: 1000px; height: 1200px;
    background: var(--black); color: var(--white);
    font-family: "Open Sans", sans-serif; overflow: hidden;
  }
  .hero-photo {
    position: absolute; left: 0; top: 0; width: 1000px; height: 700px;
    background:
      linear-gradient(180deg, rgba(10,9,10,0) 0%, rgba(10,9,10,0) 45%, rgba(10,9,10,0.85) 80%, var(--black) 100%),
      linear-gradient(180deg, var(--photo-warm) 0%, #3a3a44 30%, var(--photo-mid) 60%, var(--ink) 100%);
  }
  .club-mark {
    position: absolute; right: 40px; top: 28px; width: 190px; height: 190px;
    border-radius: 50%; background: var(--white);
    display: flex; align-items: center; justify-content: center;
    font-family: "Poppins", sans-serif; font-weight: 700; font-size: 44px; color: var(--red);
    letter-spacing: 2px;
  }
  .headline {
    position: absolute; left: 0; right: 0; top: 318px; text-align: center;
    font-family: "Poppins", sans-serif; font-weight: 700; line-height: 1;
  }
  .headline .event-name { font-size: 38px; color: var(--white); letter-spacing: 0.5px; }
  .headline .script-line {
    font-family: "Great Vibes", cursive; font-weight: 400; font-size: 56px;
    color: var(--red); margin-top: -6px; height: 52px; line-height: 52px;
  }
  .headline .line-white { font-size: 84px; font-weight: 800; color: var(--white); margin-top: 4px; }
  .headline .line-big { font-size: 106px; font-weight: 800; color: var(--red); margin-top: 4px; letter-spacing: -1px; }
  .headline .line-red { font-size: 70px; font-weight: 800; color: var(--red); margin-top: 0; }
  .event-info {
    position: absolute; left: 0; right: 0; top: 760px; text-align: center;
    font-weight: 600; font-size: 30px; line-height: 1.55;
  }
  .event-info .weekday { color: var(--red); }
  .features {
    position: absolute; left: 200px; top: 880px; list-style: none;
  }
  .features li {
    display: flex; align-items: flex-start; gap: 22px;
    font-weight: 700; font-size: 27px; line-height: 1.25;
    margin-bottom: 22px; letter-spacing: 0.5px;
  }
  .features svg { flex: none; width: 44px; height: 44px; margin-top: -4px; }
  .info-band {
    position: absolute; left: 0; bottom: 0; width: 1000px; height: 72px;
    background: var(--red); display: flex; align-items: center; justify-content: center;
    font-family: "Poppins", sans-serif; font-weight: 700; font-size: 25px; color: var(--white);
  }
</style>
</head>
<body>
<main class="poster">
  <div class="hero-photo" role="img" aria-label="Foto: Spieler von hinten vor einer Reihe beleuchteter Flipperautomaten"></div>

  <div class="club-mark" aria-label="Tischkugel Liga Kreis">TLK</div>

  <header class="headline">
    <div class="event-name">KUGELTISCH TREFFEN 2023</div>
    <div class="script-line">mit offener</div>
    <div class="line-white">NORDWALL-</div>
    <div class="line-big">TISCHKUGEL</div>
    <div class="line-red">POKAL</div>
  </header>

  <section class="event-info">
    <p>in 17492 Lindenhain/Hofbrück</p>
    <p><span class="weekday">Donnerstag</span> 18. Mai 2023 - <span class="weekday">Sonntag</span> 21. Mai 2023</p>
  </section>

  <ul class="features">
    <li>
      <svg viewBox="0 0 44 44" aria-hidden="true"><circle cx="22" cy="22" r="18" fill="none" stroke="var(--green)" stroke-width="4"/><path d="M14 22 l6 6 l11 -13" fill="none" stroke="var(--green)" stroke-width="4" stroke-linecap="round" stroke-linejoin="round"/></svg>
      <span>VIELE TURNIERE FÜR JEDERMANN</span>
    </li>
    <li>
      <svg viewBox="0 0 44 44" aria-hidden="true"><circle cx="22" cy="22" r="18" fill="none" stroke="var(--green)" stroke-width="4"/><path d="M14 22 l6 6 l11 -13" fill="none" stroke="var(--green)" stroke-width="4" stroke-linecap="round" stroke-linejoin="round"/></svg>
      <span>GROßE TOMBOLA MIT EINEM<br>FLIPPER ALS HAUPTGEWINN</span>
    </li>
    <li>
      <svg viewBox="0 0 44 44" aria-hidden="true"><circle cx="22" cy="22" r="18" fill="none" stroke="var(--green)" stroke-width="4"/><path d="M14 22 l6 6 l11 -13" fill="none" stroke="var(--green)" stroke-width="4" stroke-linecap="round" stroke-linejoin="round"/></svg>
      <span>FLIPPERSHOPS UND ZUBEHÖR</span>
    </li>
  </ul>

  <footer class="info-band">Zeitplan und weitere Informationen auf www.kugelrunde-ost.de</footer>
</main>
</body>
</html>
```